Create a Magazine Ad for an asbestos law firm

we need an 8 X 13 ad to be on the back of a magazine cover. We have the text Attached and want a similar look and feel to our website : www.harborvale-claims.example. The ad should be targeted to white males 55 years or older who are conservative and worked in industry or industrial plants. The main offer is a free case review and trying to get them to call the telephone number.

Target Market(s)

White collar men who worked in industrial plants. Age 55 years or older.

Industry/Entity Type

Legal

Requirements
Must have
• Pictures of white middle class conservative man or man and woman
Nice to have
• look at www.harborvale-claims.example to an. idea of what we are looking for

```html
<!DOCTYPE html>
<html lang="en">
<head>
<meta charset="utf-8">
<title>Mesothelioma Magazine Ad</title>
<link href="https://fonts.googleapis.com/css2?family=Poppins:wght@400;500;600;700&display=swap" rel="stylesheet">
<style>
:root{
  --brown:#8a5f28;
  --brown-dark:#5c3b15;
  --navy:#1b2a3a;
  --ink:#222;
  --beige:#e8ded1;
  --beige-deep:#d9ccbb;
  --page:#ffffff;
  --stage:#f4f4f4;
}
*{margin:0;padding:0;box-sizing:border-box}
html,body{width:1200px;height:1200px;overflow:hidden;background:var(--stage);font-family:"Poppins",sans-serif;color:var(--ink)}
.ad{position:absolute;left:312px;top:132px;width:576px;height:936px;background:var(--page);overflow:hidden}
.abs{position:absolute}
.logo-box{left:12px;top:0;width:149px;height:148px;background:var(--brown);color:#fff;font-weight:700;font-size:40px;line-height:44px;letter-spacing:2px;padding:40px 0 0 11px}
.tab-top{left:206px;top:0;width:40px;height:48px;background:var(--beige)}
.tab-right{left:535px;top:495px;width:41px;height:58px;background:var(--beige)}
.hero-photo{left:230px;top:0;width:346px;height:500px}
.headline{left:11px;top:230px;font-size:23px;font-weight:600;letter-spacing:2.5px;line-height:27px;color:var(--brown-dark)}
.headline .accent{color:var(--brown);font-weight:700}
.subhead{left:11px;top:291px;font-size:15.5px;font-weight:500;letter-spacing:1.2px;line-height:18px;color:var(--navy)}
.subhead .rule{display:inline-block;width:86px;height:2px;background:var(--brown);vertical-align:middle;margin-left:4px}
.body-copy{font-size:7.4px;font-weight:500;line-height:9.6px;color:var(--ink);width:330px}
.lead{left:11px;top:406px;font-size:11px;font-weight:600;line-height:13.5px;color:var(--ink)}
.section-title{left:11px;font-size:15px;font-weight:500;letter-spacing:1.2px;line-height:17.5px;color:var(--brown-dark)}
.section-title b{color:var(--brown);font-weight:700}
.awards{left:0;top:675px;width:576px;height:148px;background:linear-gradient(180deg,var(--beige) 0%,#efe8df 100%)}
.awards .divider{position:absolute;left:286px;top:0;width:4px;height:148px;background:#fff}
.award{position:absolute}
.pill{display:inline-block;background:linear-gradient(180deg,#9c6d30,#6e4a1b);color:#fff;font-size:14px;font-weight:500;letter-spacing:1px;padding:0 11px;height:20px;line-height:20px;border-radius:2px}
.award p{font-size:10.5px;font-weight:500;letter-spacing:.4px;margin-top:3px;color:var(--ink)}
.cta{left:11px;top:853px;width:400px;font-size:10.5px;font-weight:600;letter-spacing:.5px;line-height:12.5px;color:var(--ink)}
.cta .hl{color:var(--brown);font-weight:700}
.credit{left:11px;top:907px;font-size:7px;color:#333}
.foot-bar{left:250px;top:913px;width:326px;height:23px;background:var(--beige)}
.foot-square{left:250px;top:913px;width:49px;height:23px;background:var(--beige-deep)}
</style>
</head>
<body>
<main class="ad">
  <div class="abs logo-box">LOGO<br>HERE</div>
  <div class="abs tab-top"></div>

  <svg class="abs hero-photo" viewBox="0 0 346 500" role="img" aria-label="Photo of a smiling older man with white hair and beard, glasses and a blue shirt, holding a folder">
    <defs>
      <linearGradient id="photoTone" x1="0" y1="0" x2="1" y2="1">
        <stop offset="0" stop-color="#eef1f3"/>
        <stop offset=".55" stop-color="#a9bcd2"/>
        <stop offset="1" stop-color="#6f8fb8"/>
      </linearGradient>
    </defs>
    <path d="M30 0 H346 V495 C200 470 70 360 35 200 C25 130 20 60 30 0 Z" fill="url(#photoTone)"/>
    <path d="M18 0 C8 70 12 140 24 205 C60 370 195 485 346 500" fill="none" stroke="#e2e2e2" stroke-width="10"/>
  </svg>
  <div class="abs tab-right"></div>

  <h1 class="abs headline">DIAGNOSED WITH<br><span class="accent">MESOTHELIOMA,</span></h1>
  <h2 class="abs subhead">YOU COULD BE OWED<br>COMPENSATION<span class="rule"></span></h2>

  <p class="abs body-copy" style="left:11px;top:335px">It's very likely you developed this disease through asbestos exposure. Mesothelioma patients are getting multi-million dollar settlements, decades later, from:</p>
  <p class="abs body-copy" style="left:11px;top:372px">• Exposure to asbestos products,<br>• Ex-employers, or<br>• Talcum baby powder companies.</p>

  <p class="abs lead">We can help you find out if you<br>qualify for a case in minutes.</p>
  <p class="abs body-copy" style="left:11px;top:441px">• We'll analyze your situation at no cost<br>• Determine how much compensation you could be entitled<br>• too Show you the next steps to get what you're owed</p>

  <h2 class="abs section-title" style="top:478px"><b>$30 BILLION</b> IS AVAILABLE IN<br>TRUST FOR <b>MESOTHELIOMA</b> PATIENTS</h2>
  <p class="abs body-copy" style="left:11px;top:518px">Tradesmen in many industries were negligently exposed to asbestos materials well into the 1990s. Whether you developed Mesothelioma yourself due to asbestos exposure or you're the surviving family of a lost loved one you could be entitled to significant compensation.</p>

  <h2 class="abs section-title" style="top:573px">HOW MUCH MONEY CAN PEOPLE RECEIVE<br>FROM A <b>MESOTHELIOMA CASE?</b></h2>
  <p class="abs body-copy" style="left:11px;top:616px">Depending on where you were exposed and a few other factors, you can get a settlement from 6 to 7 figures. Here are a few examples of Mesothelioma Settlements received by our clients. These figures are the total compensation after all attorney fees and expenses are deducted.</p>

  <section class="abs awards">
    <div class="divider"></div>
    <div class="award" style="left:11px;top:7px"><span class="pill">$6,142,500</span><p>Exposed through heavy duty vehicles</p></div>
    <div class="award" style="left:11px;top:57px"><span class="pill">$6,033,510</span><p>Exposed through general contracting</p></div>
    <div class="award" style="left:11px;top:104px"><span class="pill">$5,939,010</span><p>Exposed through boat repair</p></div>
    <div class="award" style="left:333px;top:7px"><span class="pill">$3,921,750</span><p>Exposed through navy service</p></div>
    <div class="award" style="left:333px;top:57px"><span class="pill">$3,600,450</span><p>Exposed through navy service</p></div>
    <div class="award" style="left:333px;top:104px"><span class="pill">$2.5 Million</span><p>Exposed from Brightwell Talcum Baby Powder</p></div>
  </section>

  <p class="abs cta"><span class="hl">FIND OUT IF YOU'RE ELIGIBLE, FOR FREE, IN MINUTES.</span> We'll evaluate your situation and tell you what your case could be worth. <span class="hl">GET YOUR FREE EVALUATION NOW! CALL 1-XXX XXXX (GOOD NUMBER)</span></p>
  <p class="abs credit">Harborvale Claims, LLP, Martin Ellery, Galveston, TX</p>
  <div class="abs foot-bar"></div>
  <div class="abs foot-square"></div>
</main>
</body>
</html>
```